Personal Development company in need for a fun website

QV7 effectively encourages personal growth and self-improvement by providing the positive tools which will motivate, enlighten and empower the client in a relaxed, friendly environment. Taking care of the ‘self’ is essential to being productive and valuable in all aspects of life, professionally and personally. We want it to be edgy and fun targeting professionals, youth and women entering the workforce.

We would need a homepage that would have a news and features, an online shop for some of our products, a schedule for our events and workshops, a calendar, an about us section and team. Other features that need to be added terms and conditions, privacy, link to social media on the bottom of the home page.

Please look at brain yard and the hall of days to understand our concept.

Target Market(s)

Young professionals, women that want to enter the workplace, individuals of all ages seeking personal development in all its forms.

Industry/Entity Type

It Company

Coding

Coded - Design and coding required

Number of Pages Required

5+ page

Font styles to use
Sans Serif

Requirements
Must have
• Must be clean and attractive.
Nice to have
• Graphic design work
Should not have
• Photographs, unless its the speaker of an event.

```html
<!DOCTYPE html>
<html lang="en">
<head>
<meta charset="utf-8">
<title>QV7 – Personal Development</title>
<link href="https://fonts.googleapis.com/css2?family=Raleway:wght@400;500;600&family=Open+Sans:wght@400;600&display=swap" rel="stylesheet">
<style>
  :root {
    --blue: #1d2bb8;
    --navy: #1a2a9c;
    --orange: #f0960c;
    --burnt: #df6413;
    --red: #c4122f;
    --footer: #b3001e;
    --ink: #333;
    --grey: #6b6b6b;
    --paper: #ffffff;
    --mist: #f1f2f4;
  }
  * { margin: 0; padding: 0; box-sizing: border-box; }
  h1, h2, h3 { font-weight: 400; }
  html, body { width: 668px; height: 1200px; overflow: hidden; background: var(--paper); }
  body { position: relative; font-family: "Open Sans", sans-serif; color: var(--ink); }
  .abs { position: absolute; }

  /* header */
  .brand { left: 100px; top: 14px; }
  .brand-name { font-family: "Raleway", sans-serif; font-weight: 600; font-size: 24px; color: var(--blue); }

  .main-nav { left: 0; top: 55px; width: 668px; height: 26px; background: var(--blue); }
  .main-nav ul { list-style: none; display: flex; margin-left: 100px; height: 100%; }
  .main-nav li { font-family: "Raleway", sans-serif; font-size: 8.5px; color: #fff; padding: 0 13px; line-height: 26px; border-right: 1px solid rgba(255,255,255,.25); }
  .main-nav li.active { background: var(--orange); padding: 0 15px; }

  /* hero */
  .hero { left: 0; top: 81px; width: 668px; height: 266px; background: linear-gradient(180deg, #6d7278 0%, #4b4f52 45%, #3a3628 75%, #6a5a3a 100%); }
  .hero-curve { left: 0; top: 320px; }
  .hero-arrow { top: 174px; width: 22px; height: 40px; background: rgba(0,0,0,.45); color: #fff; font-size: 16px; line-height: 40px; text-align: center; }
  .hero-title { left: 0; width: 668px; top: 155px; text-align: center; font-family: "Raleway", sans-serif; font-weight: 500; font-size: 31px; color: #fff; letter-spacing: .5px; }
  .hero-sub { left: 0; width: 668px; top: 197px; text-align: center; font-weight: 600; font-size: 13px; color: #fff; }
  .btn-outline { border: 1px solid #fff; color: #fff; font-size: 8.5px; text-align: center; }
  .hero-btn { left: 297px; top: 222px; width: 72px; height: 21px; line-height: 19px; }
  .emblem { left: 304px; top: 322px; width: 64px; height: 40px; text-align: center; font-family: "Raleway", sans-serif; font-weight: 600; font-size: 15px; color: var(--blue); line-height: 48px; }

  /* about */
  .about-title { left: 0; width: 668px; top: 380px; text-align: center; font-family: "Raleway", sans-serif; font-weight: 500; font-size: 16.5px; color: var(--burnt); }
  .about-text { left: 118px; width: 432px; text-align: center; font-size: 6.4px; line-height: 10px; color: var(--grey); }

  /* personal growth band */
  .growth { left: 0; top: 504px; width: 668px; height: 220px; background: radial-gradient(ellipse at 28% 50%, #ffe07a 0%, #f59a1a 22%, #b4480c 50%, #3f1a08 80%, #2a1f1c 100%); }
  .growth-title { left: 330px; top: 560px; font-family: "Raleway", sans-serif; font-size: 16.5px; line-height: 20px; color: #fff; }
  .growth-text { left: 330px; top: 606px; width: 246px; font-size: 6.4px; line-height: 10px; color: #fff; }
  .growth-btn { left: 332px; top: 647px; width: 70px; height: 21px; line-height: 19px; }

  /* features */
  .features { left: 0; top: 724px; width: 668px; height: 226px; background: linear-gradient(160deg, #fafafa 0%, var(--mist) 60%, #e8e9ec 100%); }
  .features-title { left: 0; width: 668px; top: 744px; text-align: center; font-family: "Raleway", sans-serif; font-size: 16px; color: #333; }
  .feature-icon { width: 56px; height: 56px; border: 1px dashed #b8b8b8; border-radius: 50%; display: flex; align-items: center; justify-content: center; }
  .feature-name { font-family: "Raleway", sans-serif; font-size: 10.5px; color: var(--red); }
  .feature-text { width: 160px; font-size: 6.2px; line-height: 9px; color: var(--grey); }

  /* news */
  .news { left: 0; top: 950px; width: 668px; height: 180px; background: linear-gradient(100deg, #d49a66 0%, #e9c7a6 35%, #c7ccd3 65%, #51617a 100%); }
  .news-title { left: 100px; top: 978px; font-family: "Raleway", sans-serif; font-size: 17px; color: #2a2a2a; }
  .news-card { top: 1008px; width: 154px; height: 82px; background: linear-gradient(180deg, #fff 0%, #f2f2f2 100%); }
  .news-card h3 { position: absolute; left: 14px; top: 11px; font-weight: 600; font-size: 7.8px; color: var(--navy); }
  .news-card p { position: absolute; left: 14px; top: 25px; width: 130px; font-size: 6px; line-height: 9.5px; color: var(--grey); }
  .news-date { position: absolute; left: 0; bottom: 0; width: 63px; height: 14px; background: var(--navy); color: #fff; font-size: 6px; line-height: 14px; padding-left: 8px; }

  /* footer */
  .site-footer { left: 0; top: 1130px; width: 668px; height: 70px; background: var(--footer); color: #fff; }
  .footer-nav { left: 100px; top: 1149px; display: flex; gap: 15px; font-size: 7px; color: #fff; list-style: none; }
  .copyright { left: 100px; top: 1166px; font-size: 6px; color: #fff; }
  .legal { left: 461px; top: 1149px; font-size: 6.2px; color: #fff; }
  .social { left: 509px; top: 1162px; }
</style>
</head>
<body>

<header>
  <div class="abs brand"><span class="brand-name">QV7</span></div>
  <nav class="abs main-nav">
    <ul>
      <li class="active">HOME</li>
      <li>NEWS</li>
      <li>SHOP</li>
      <li>EVENTS &amp; WORKSHOP</li>
      <li>CALENDAR</li>
      <li>ABOUT US</li>
      <li>CONTACT US</li>
    </ul>
  </nav>
</header>

<section>
  <div class="abs hero" role="img" aria-label="City skyscrapers at dusk above a busy street"></div>
  <svg class="abs hero-curve" width="668" height="30" viewBox="0 0 668 30">
    <path d="M0 8 Q334 30 668 8 L668 30 L0 30 Z" fill="#fff"/>
    <path d="M300 30 A36 36 0 0 1 368 30 Z" fill="#fff"/>
  </svg>
  <div class="abs hero-arrow" style="left:0">&#8249;</div>
  <div class="abs hero-arrow" style="left:646px">&#8250;</div>
  <h1 class="abs hero-title">MOTIVATIONAL GROWTH</h1>
  <p class="abs hero-sub">SUSPENDISSE QUAM LEO MOLESTIE</p>
  <div class="abs btn-outline hero-btn">Learn More</div>
  <div class="abs emblem">QV7</div>
</section>

<section>
  <h2 class="abs about-title">ABOUT OUR COMPANY</h2>
  <p class="abs about-text" style="top:410px">Morbi diam mauris viverra in gravida eu mattis in ante Morbi eget arcu Morbi porta libero id ullamcorper nonummy nibh ligula pulvinar metus eget consectetuer augue nisi quis lacus Ut ac mi quis lacus mollis aliquam Curabitur iaculis</p>
  <p class="abs about-text" style="top:435px">tempus eros Curabitur vel mi sit amet magna malesuada ultrices Ut nisi erat fermentum vel congue id euismod in elit Fusce ultricies orci ac feugiat suscipit leo massa sodales velit et scelerisque mi tortor at ipsum cligula augue bibendum accumsan vestibulum ut commodo a mi Morbi ornare gravida elit Integer congue augue et malesuada iaculis ipsum dui aliquet felis at cursus magna nisl nec elit vm</p>
</section>

<section>
  <div class="abs growth" role="img" aria-label="Bright orange light burst with a personal growth emblem"></div>
  <h2 class="abs growth-title">QV7 effectively encourages<br>Personal growth</h2>
  <p class="abs growth-text">Morbi diam mauris viverra in gravida eu mattis in ante Morbi eget arcu Morbi porta libero id ullamcorper nonummy nibh ligula pulvinar metus eget consectetuer augue nisi quis lacus Ut ac</p>
  <div class="abs btn-outline growth-btn">Learn More</div>
</section>

<section>
  <div class="abs features"></div>
  <h2 class="abs features-title">Our Features</h2>

  <div class="abs feature-icon" style="left:100px;top:780px"><svg width="22" height="22"><circle cx="11" cy="11" r="9" fill="#f0960c"/></svg></div>
  <h3 class="abs feature-name" style="left:161px;top:789px">Motivation</h3>
  <p class="abs feature-text" style="left:161px;top:804px">gravida eu mattis in ante Morbi eget arcu Morbi porta libero id ullamcorper nonummy nibh ligula pulvinar</p>

  <div class="abs feature-icon" style="left:338px;top:780px"><svg width="22" height="22"><circle cx="11" cy="11" r="9" fill="#f0960c"/></svg></div>
  <h3 class="abs feature-name" style="left:406px;top:789px">Encorage &amp; Growth</h3>
  <p class="abs feature-text" style="left:406px;top:804px">gravida eu mattis in ante Morbi eget arcu Morbi porta libero id ullamcorper nonummy nibh</p>

  <div class="abs feature-icon" style="left:100px;top:852px"><svg width="22" height="22"><circle cx="11" cy="11" r="9" fill="#f0960c"/></svg></div>
  <h3 class="abs feature-name" style="left:162px;top:863px">Personal Development</h3>
  <p class="abs feature-text" style="left:162px;top:878px">gravida eu mattis in ante Morbi eget arcu Morbi porta libero id ullamcorper nonummy nibh ligu</p>

  <div class="abs feature-icon" style="left:338px;top:852px"><svg width="22" height="22"><circle cx="11" cy="11" r="9" fill="#f0960c"/></svg></div>
  <h3 class="abs feature-name" style="left:406px;top:863px">Consulting</h3>
  <p class="abs feature-text" style="left:406px;top:878px">gravida eu mattis in ante Morbi eget arcu Morbi porta libero id ullamcorper nonummy nibh</p>
</section>

<section>
  <div class="abs news" role="img" aria-label="Glass roof of a modern building with city towers beyond"></div>
  <h2 class="abs news-title">Latest News</h2>
  <article class="abs news-card" style="left:98px">
    <h3>Aultricies orci ac feugiat</h3>
    <p>suscipit leo massa sodales velit et scelerisque mi tortor at ipsum cligula augue bibendum accumsan vestibulum ut commodo</p>
    <span class="news-date">25 JAN 2016</span>
  </article>
  <article class="abs news-card" style="left:254px">
    <h3>Duis quam Nam eget</h3>
    <p>suscipit leo massa sodales velit et scelerisque mi tortor at ipsum cligula augue bibendum accumsan vestibulum ut commodo</p>
    <span class="news-date">25 JAN 2016</span>
  </article>
  <article class="abs news-card" style="left:411px">
    <h3>Integer orci tellus tristique</h3>
    <p>suscipit leo massa sodales velit et scelerisque mi tortor at ipsum cligula augue bibendum accumsan vestibulum ut commodo</p>
    <span class="news-date">25 JAN 2016</span>
  </article>
</section>

<footer>
  <div class="abs site-footer"></div>
  <ul class="abs footer-nav">
    <li>Home</li><li>News</li><li>Shop</li><li>Events &amp; Workshop</li><li>Calendar</li><li>About us</li><li>Contact us</li>
  </ul>
  <p class="abs copyright">© 2016 Company Name &nbsp;All right reserved</p>
  <p class="abs legal">Privacy Policy &nbsp;| &nbsp;Terms &amp; conditions</p>
  <svg class="abs social" width="60" height="16" viewBox="0 0 60 16">
    <circle cx="8" cy="8" r="6.5" fill="none" stroke="#fff" stroke-width="1"/>
    <circle cx="22.5" cy="8" r="6.5" fill="none" stroke="#fff" stroke-width="1"/>
    <circle cx="37" cy="8" r="6.5" fill="none" stroke="#fff" stroke-width="1"/>
    <circle cx="51.5" cy="8" r="6.5" fill="none" stroke="#fff" stroke-width="1"/>
  </svg>
</footer>

</body>
</html>
```